Website banner

Here is the link where the current banner is featured https://www.brimlark.com.au/collections/gel-blasters

I need the banner recreated into desktop and mobile format size.
Update the key points to:
- FREE SHIPPING AUSTRALIA WIDE
- SAME DAY DISPATCH
- BEST PRICE GUARANTEE
- 3000+ 5 STAR REVIEWS
- BEST SERVICE & WARRANTY
- 100% SECURE CHECKOUT

I want the banner to suit the style of the website and make it look better than the last graphic.

I also need the "save even more" picture to be recreated as it looks very plain at the moment,

```html
<!DOCTYPE html>
<html lang="en">
<head>
<meta charset="utf-8">
<title>Brimlark Banner Set</title>
<link href="https://fonts.googleapis.com/css2?family=Poppins:wght@400;500;700;800&family=Mr+Dafoe&display=swap" rel="stylesheet">
<style>
  :root {
    --board: #1e1e1e;
    --panel: #0d0d0d;
    --photo-dark: #141414;
    --photo-mid: #3a3a3a;
    --red: #e01e26;
    --white: #ffffff;
  }
  * { margin: 0; padding: 0; box-sizing: border-box; }
  html, body { width: 1200px; height: 686px; overflow: hidden; background: var(--board); }
  .board { position: relative; width: 1200px; height: 686px; font-family: "Poppins", sans-serif; color: var(--white); }

  .format-label { position: absolute; font-family: "Mr Dafoe", cursive; font-size: 62px; line-height: 1; color: var(--white); z-index: 5; }
  .format-label--web { left: 96px; top: 44px; }
  .format-label--mobile { left: 40px; top: 268px; }
  .format-label--other { left: 985px; top: 420px; }

  .banner { position: absolute; overflow: hidden; background: var(--panel); }
  .banner__photo { position: absolute; inset: 0;
    background: radial-gradient(ellipse at 35% 30%, var(--photo-mid) 0%, var(--photo-dark) 55%, #080808 100%); }
  .banner__grunge { position: absolute; left: 0; bottom: 0; width: 100%; }

  .banner--web { left: 142px; top: 36px; width: 917px; height: 183px; }
  .banner--web .banner__grunge { height: 50px; }
  .features--web { position: absolute; left: 70px; top: 54px; width: 790px; display: grid; grid-template-columns: repeat(6, 1fr); }
  .features--web .feature__icon { width: 30px; height: 30px; }
  .features--web .feature__lead { font-size: 7px; margin-top: 8px; letter-spacing: .4px; }
  .features--web .feature__key { font-size: 9.5px; }

  .banner--mobile { left: 142px; top: 250px; width: 562px; height: 355px; }
  .banner--mobile .banner__grunge { height: 72px; }
  .features--mobile { position: absolute; left: 20px; top: 45px; width: 540px; display: grid; grid-template-columns: repeat(3, 1fr); row-gap: 26px; }
  .features--mobile .feature__icon { width: 58px; height: 58px; }
  .features--mobile .feature__lead { font-size: 15px; margin-top: 12px; letter-spacing: .8px; }
  .features--mobile .feature__key { font-size: 20px; }

  .feature { display: flex; flex-direction: column; align-items: center; text-align: center; }
  .feature__icon { fill: none; stroke: var(--white); stroke-width: 1.6; stroke-linejoin: round; stroke-linecap: round; }
  .feature__lead { font-weight: 500; line-height: 1.2; text-transform: uppercase; }
  .feature__key { font-weight: 800; color: var(--red); line-height: 1.1; text-transform: uppercase; }

  .offer { position: absolute; left: 713px; top: 250px; width: 345px; height: 185px; background: var(--panel); overflow: hidden; }
  .offer__stroke { position: absolute; left: 22px; top: 3px; width: 318px; height: 52px; }
  .offer__title { position: absolute; left: 22px; top: 11px; width: 318px; text-align: center; font-weight: 800; font-size: 24px; letter-spacing: .3px; }
  .offer__tiers { position: absolute; left: 43px; top: 71px; list-style: none; }
  .offer__tier { display: flex; font-size: 17px; font-weight: 500; line-height: 29px; }
  .offer__spend { width: 178px; }
  .offer__save { font-weight: 800; font-size: 19px; color: var(--red); }
  .offer .banner__grunge { height: 30px; }
</style>
</head>
<body>
<div class="board">

  <span class="format-label format-label--web">Web</span>
  <span class="format-label format-label--mobile">Mobile</span>
  <span class="format-label format-label--other">Other</span>

  <!-- Desktop banner -->
  <section class="banner banner--web">
    <div class="banner__photo" role="img" aria-label="Dark monochrome photo of soldiers in tactical gear"></div>
    <svg class="banner__grunge" viewBox="0 0 100 20" preserveAspectRatio="none" aria-hidden="true">
      <path fill="var(--red)" d="M0 8 L3 9 L5 6 L8 10 L11 7 L14 11 L17 8 L20 12 L24 9 L27 11 L31 8 L35 12 L39 9 L43 11 L47 8 L51 11 L55 9 L58 12 L62 7 L66 10 L70 6 L73 8 L77 4 L81 6 L85 3 L89 5 L93 3 L97 6 L100 4 L100 20 L0 20 Z"/>
    </svg>
    <div class="features features--web">
      <div class="feature">
        <svg class="feature__icon" viewBox="0 0 40 40"><path d="M20 4c-7 0-12 5-12 12 0 9 12 20 12 20s12-11 12-20c0-7-5-12-12-12z"/><circle cx="20" cy="16" r="4"/></svg>
        <span class="feature__lead">Free Shipping</span><span class="feature__key">Australia Wide</span>
      </div>
      <div class="feature">
        <svg class="feature__icon" viewBox="0 0 40 40"><path d="M6 16a14 12 0 0 1 28 0z"/><path d="M6 16l8 8M34 16l-8 8M20 16v8"/><rect x="13" y="24" width="14" height="12"/><path d="M13 24l14 12M27 24l-14 12"/></svg>
        <span class="feature__lead">Same Day</span><span class="feature__key">Dispatch</span>
      </div>
      <div class="feature">
        <svg class="feature__icon" viewBox="0 0 40 40"><path d="M20 5l12 5v9c0 8-6 14-12 16-6-2-12-8-12-16v-9z"/><path d="M24 15h-5a2.5 2.5 0 0 0 0 5h2a2.5 2.5 0 0 1 0 5h-5M20 12v3M20 25v3"/></svg>
        <span class="feature__lead">Best Price</span><span class="feature__key">Guarantee</span>
      </div>
      <div class="feature">
        <svg class="feature__icon" viewBox="0 0 40 40"><path d="M8 6l1.5 3 3 .3-2.3 2 .7 3-2.9-1.6-2.9 1.6.7-3-2.3-2 3-.3zM20 6l1.5 3 3 .3-2.3 2 .7 3-2.9-1.6-2.9 1.6.7-3-2.3-2 3-.3zM32 6l1.5 3 3 .3-2.3 2 .7 3-2.9-1.6-2.9 1.6.7-3-2.3-2 3-.3zM8 18l1.5 3 3 .3-2.3 2 .7 3-2.9-1.6-2.9 1.6.7-3-2.3-2 3-.3zM20 18l1.5 3 3 .3-2.3 2 .7 3-2.9-1.6-2.9 1.6.7-3-2.3-2 3-.3zM8 30l1.5 3 3 .3-2.3 2 .7 3-2.9-1.6-2.9 1.6.7-3-2.3-2 3-.3z"/><path d="M27 24h8M16 36h19"/></svg>
        <span class="feature__lead">3000+</span><span class="feature__key">5 Star Reviews</span>
      </div>
      <div class="feature">
        <svg class="feature__icon" viewBox="0 0 40 40"><path d="M8 22v-4a12 12 0 0 1 24 0v4"/><rect x="5" y="20" width="6" height="10" rx="2"/><rect x="29" y="20" width="6" height="10" rx="2"/><path d="M32 30c0 4-4 6-10 6"/><rect x="17" y="34" width="6" height="4" rx="1"/></svg>
        <span class="feature__lead">Best Service</span><span class="feature__key">+ Warranty</span>
      </div>
      <div class="feature">
        <svg class="feature__icon" viewBox="0 0 40 40"><rect x="4" y="5" width="32" height="30" rx="2"/><path d="M4 11h32M8 8h1M11 8h1M14 8h1"/><circle cx="20" cy="23" r="8"/><rect x="16.5" y="22" width="7" height="6" rx="1"/><path d="M18 22v-2a2 2 0 0 1 4 0v2"/></svg>
        <span class="feature__lead">100% Secure</span><span class="feature__key">Checkout</span>
      </div>
    </div>
  </section>

  <!-- Mobile banner -->
  <section class="banner banner--mobile">
    <div class="banner__photo" role="img" aria-label="Dark monochrome photo of soldiers in tactical gear"></div>
    <svg class="banner__grunge" viewBox="0 0 100 20" preserveAspectRatio="none" aria-hidden="true">
      <path fill="var(--red)" d="M0 6 L4 8 L7 5 L10 9 L14 6 L18 9 L22 7 L26 10 L30 8 L34 11 L38 8 L42 10 L46 7 L50 10 L54 8 L58 11 L62 8 L66 10 L70 7 L74 9 L78 6 L82 9 L86 6 L90 8 L94 5 L97 7 L100 5 L100 20 L0 20 Z"/>
    </svg>
    <div class="features features--mobile">
      <div class="feature">
        <svg class="feature__icon" viewBox="0 0 40 40"><path d="M20 4c-7 0-12 5-12 12 0 9 12 20 12 20s12-11 12-20c0-7-5-12-12-12z"/><circle cx="20" cy="16" r="4"/></svg>
        <span class="feature__lead">Free Shipping</span><span class="feature__key">Australia Wide</span>
      </div>
      <div class="feature">
        <svg class="feature__icon" viewBox="0 0 40 40"><path d="M6 16a14 12 0 0 1 28 0z"/><path d="M6 16l8 8M34 16l-8 8M20 16v8"/><rect x="13" y="24" width="14" height="12"/><path d="M13 24l14 12M27 24l-14 12"/></svg>
        <span class="feature__lead">Same Day</span><span class="feature__key">Dispatch</span>
      </div>
      <div class="feature">
        <svg class="feature__icon" viewBox="0 0 40 40"><path d="M20 5l12 5v9c0 8-6 14-12 16-6-2-12-8-12-16v-9z"/><path d="M24 15h-5a2.5 2.5 0 0 0 0 5h2a2.5 2.5 0 0 1 0 5h-5M20 12v3M20 25v3"/></svg>
        <span class="feature__lead">Best Price</span><span class="feature__key">Guarantee</span>
      </div>
      <div class="feature">
        <svg class="feature__icon" viewBox="0 0 40 40"><path d="M8 6l1.5 3 3 .3-2.3 2 .7 3-2.9-1.6-2.9 1.6.7-3-2.3-2 3-.3zM20 6l1.5 3 3 .3-2.3 2 .7 3-2.9-1.6-2.9 1.6.7-3-2.3-2 3-.3zM32 6l1.5 3 3 .3-2.3 2 .7 3-2.9-1.6-2.9 1.6.7-3-2.3-2 3-.3zM8 18l1.5 3 3 .3-2.3 2 .7 3-2.9-1.6-2.9 1.6.7-3-2.3-2 3-.3zM20 18l1.5 3 3 .3-2.3 2 .7 3-2.9-1.6-2.9 1.6.7-3-2.3-2 3-.3zM8 30l1.5 3 3 .3-2.3 2 .7 3-2.9-1.6-2.9 1.6.7-3-2.3-2 3-.3z"/><path d="M27 24h8M16 36h19"/></svg>
        <span class="feature__lead">3000+</span><span class="feature__key">5 Star Reviews</span>
      </div>
      <div class="feature">
        <svg class="feature__icon" viewBox="0 0 40 40"><path d="M8 22v-4a12 12 0 0 1 24 0v4"/><rect x="5" y="20" width="6" height="10" rx="2"/><rect x="29" y="20" width="6" height="10" rx="2"/><path d="M32 30c0 4-4 6-10 6"/><rect x="17" y="34" width="6" height="4" rx="1"/></svg>
        <span class="feature__lead">Best Service</span><span class="feature__key">+ Warranty</span>
      </div>
      <div class="feature">
        <svg class="feature__icon" viewBox="0 0 40 40"><rect x="4" y="5" width="32" height="30" rx="2"/><path d="M4 11h32M8 8h1M11 8h1M14 8h1"/><circle cx="20" cy="23" r="8"/><rect x="16.5" y="22" width="7" height="6" rx="1"/><path d="M18 22v-2a2 2 0 0 1 4 0v2"/></svg>
        <span class="feature__lead">100% Secure</span><span class="feature__key">Checkout</span>
      </div>
    </div>
  </section>

  <!-- Volume discount tile -->
  <section class="offer">
    <svg class="offer__stroke" viewBox="0 0 100 20" preserveAspectRatio="none" aria-hidden="true">
      <path fill="var(--red)" d="M2 3 L10 1 L30 2 L50 0 L70 2 L90 1 L99 3 L97 8 L100 12 L96 16 L98 19 L80 18 L60 20 L40 18 L20 20 L4 18 L1 14 L3 10 L0 6 Z"/>
    </svg>
    <h2 class="offer__title">SAVE EVEN MORE!</h2>
    <ul class="offer__tiers">
      <li class="offer__tier"><span class="offer__spend">ORDER $250 + GET</span><span class="offer__save">5% OFF</span></li>
      <li class="offer__tier"><span class="offer__spend">ORDER $500 + GET</span><span class="offer__save">10% OFF</span></li>
      <li class="offer__tier"><span class="offer__spend">ORDER $1000 + GET</span><span class="offer__save">15% OFF</span></li>
    </ul>
    <svg class="banner__grunge" viewBox="0 0 100 20" preserveAspectRatio="none" aria-hidden="true">
      <path fill="var(--red)" d="M0 10 L5 12 L10 8 L16 13 L22 10 L28 14 L34 11 L40 14 L46 12 L52 15 L58 11 L64 14 L70 10 L76 13 L82 9 L88 12 L94 8 L100 11 L100 20 L0 20 Z"/>
    </svg>
  </section>

</div>
</body>
</html>
```